Estate Agent A5 Doublesided leaflet

We would like to have a very vibrant, simple, elegant and memorable leaflet promoting our sales division launch and the special offer of only 0.5% fee for instructions received in March 2015

Target Market(s)

Our customers usually have properties valued 500,000USD or more

Industry/Entity Type

Sales

Requirements
Must have
• originality, easy to remember, clear message to client
Something unique, as in the leaflet attached below

```html
<!DOCTYPE html>
<html lang="en">
<head>
<meta charset="utf-8">
<title>Estate Agent Leaflet – Sales Launch</title>
<link rel="stylesheet" href="https://fonts.googleapis.com/css2?family=Bungee&family=Quicksand:wght@500;700&display=swap">
<style>
  :root {
    --paper: #ffffff;
    --offer-red: #ff2a2a;
    --offer-yellow: #ffc81a;
    --offer-orange: #ff8a1f;
    --offer-green: #1fbf55;
    --head-green: #1aa84f;
    --head-yellow: #f5bd12;
    --head-red: #e5232b;
    --shade: rgba(38, 36, 34, 0.72);
    --photo-light: #c9b48c;
    --photo-deep: #a89370;
    --logo-green: #10a957;
  }
  * { margin: 0; padding: 0; box-sizing: border-box; }
  html, body { width: 1200px; height: 423px; overflow: hidden; background: var(--paper); }
  .leaflet { position: relative; width: 1200px; height: 423px; background: var(--paper); }

  .front { position: absolute; left: 0; top: 0; width: 600px; height: 423px; overflow: hidden; }
  .photo {
    position: absolute; inset: 0;
    background: linear-gradient(160deg, var(--photo-light) 0%, var(--photo-deep) 100%);
  }
  .shade { position: absolute; left: 0; top: 163px; width: 600px; height: 260px; background: var(--shade); }
  .offer {
    position: absolute; left: 0; top: 168px; width: 600px;
    text-align: center; list-style: none;
    font-family: "Bungee", "Quicksand", sans-serif;
    font-size: 36px; line-height: 37.5px; letter-spacing: -1.5px;
    color: transparent;
    -webkit-text-stroke-width: 2.5px;
  }
  .offer .red { -webkit-text-stroke-color: var(--offer-red); }
  .offer .yellow { -webkit-text-stroke-color: var(--offer-yellow); }
  .offer .orange { -webkit-text-stroke-color: var(--offer-orange); }
  .offer .green { -webkit-text-stroke-color: var(--offer-green); }

  .back { position: absolute; left: 600px; top: 0; width: 600px; height: 423px; }
  .headline {
    position: absolute; left: 60px; top: 103px; width: 290px;
    text-align: center;
    font-family: "Quicksand", sans-serif; font-weight: 500;
    font-size: 31px; line-height: 36px;
  }
  .headline .green { color: var(--head-green); }
  .headline .yellow { color: var(--head-yellow); }
  .headline .red { color: var(--head-red); }
  .feature-photo {
    position: absolute; left: 78px; top: 218px; width: 264px; height: 182px;
    background: linear-gradient(160deg, var(--photo-light) 0%, var(--photo-deep) 100%);
  }
  .brand {
    position: absolute; left: 450px; top: 318px; width: 133px; height: 82px;
    background: var(--logo-green);
    display: flex; align-items: center; justify-content: center;
    text-align: center;
    font-family: "Quicksand", sans-serif; font-weight: 700;
    font-size: 15px; line-height: 21px; letter-spacing: 2px;
    color: var(--paper);
  }
</style>
</head>
<body>
  <main class="leaflet">
    <section class="front">
      <div class="photo" role="img" aria-label="Photo of two open hands holding a small model house with a red roof above a wheat field"></div>
      <div class="shade"></div>
      <ul class="offer">
        <li class="red">Special offer</li>
        <li class="yellow">of only 0.5%</li>
        <li class="orange">fee for</li>
        <li class="green">instructions</li>
        <li class="orange">received in</li>
        <li class="red">March 2015</li>
      </ul>
    </section>
    <section class="back">
      <h1 class="headline">
        <span class="green">FRESH HOME</span><br>
        <span class="yellow">READY FOR YOU</span><br>
        <span class="red">TO MOVE ON</span>
      </h1>
      <div class="feature-photo" role="img" aria-label="Photo of hands holding a small model house with a red roof in front of a field"></div>
      <div class="brand">YOUR<br>LOGO</div>
    </section>
  </main>
</body>
</html>
```